Investment Management Client Email Template

We need an email template to send out monthly returns of our investment strategies to all clients as well as quarterly investment letters. We want to see an elegant somewhat simple design (not overly graphic) that portrays exclusivity, experience, expertise. Nothing playful or too high tech. Our clients are often high net worth middle age or older. We have also won several awards which are included in the attachments along with our logo. We will want to email a letter as the body or a chart. We should have room for a disclaimer at the bottom. The attachments can be used in the design of the graphics.

Target Market(s)

high net worth clientelle

Industry/Entity Type

Financial Planning

Requirements
Must have
• a clean elegant design with the majority of the body being a chart or text as in a letter. use the colors of the logo - blues, grays blacks. Design must look good in outlook or on an iPhone.
• There should be a space for text as the body, a disclaimer at the bottom and an address at the bottom.
Should not have
• Overly graphic. Highlight should be the chart (table) or text. Graphics should make the template look professional but not overly busy.

```html
<!DOCTYPE html>
<html lang="en">
<head>
<meta charset="utf-8">
<title>Harbor Ridge Management &amp; Research – Client Letter</title>
<link href="https://fonts.googleapis.com/css2?family=Open+Sans:wght@400;600;700&display=swap" rel="stylesheet">
<style>
  :root {
    --ink: #111111;
    --band-black: #000000;
    --footer-black: #121212;
    --brand-blue: #2c3590;
    --accent-blue: #6166b0;
    --muted-gray: #7a7a7a;
    --footer-text: #c9c9c9;
    --base-gray: #6a6a6a;
    --white: #ffffff;
  }
  * { margin: 0; padding: 0; box-sizing: border-box; }
  html, body { width: 867px; height: 1200px; overflow: hidden; background: var(--white); }
  body { font-family: "Open Sans", Arial, sans-serif; color: var(--ink); }
  .letter { position: relative; width: 867px; height: 1200px; overflow: hidden; background: var(--white); }

  .brand { position: absolute; left: 56px; top: 50px; display: flex; align-items: center; gap: 12px; }
  .brand-square { width: 46px; height: 46px; background: var(--brand-blue); }
  .brand-name { color: var(--brand-blue); font-weight: 600; font-size: 19px; line-height: 24px; }

  .issue-date { position: absolute; left: 692px; top: 66px; font-size: 19px; color: var(--muted-gray); }
  .issue-date b { font-weight: 700; }

  .hero { position: absolute; left: 0; top: 135px; width: 867px; height: 282px; }
  .hero-title { position: absolute; left: 124px; top: 222px; color: var(--white); font-weight: 700; font-size: 58px; line-height: 70px; }

  .letter-body { position: absolute; left: 162px; top: 442px; width: 592px; font-size: 13.4px; line-height: 19.5px; text-align: justify; }
  .letter-body p + p { margin-top: 19.5px; }

  .awards { position: absolute; left: 0; top: 826px; width: 867px; height: 119px;
    background: linear-gradient(#f4f4f5 0%, #d2d3d6 45%, #c7c8cb 60%, #e8e8ea 100%); }
  .awards-divider { position: absolute; top: 18px; width: 1px; height: 82px; background: #b4b5b8; }
  .award { position: absolute; box-shadow: 3px 4px 6px rgba(0,0,0,0.35); }
  .award-plaque { left: 71px; top: 25px; width: 104px; height: 58px; background: #ffffff; border-bottom: 10px solid #b3222a; }
  .award-seal { left: 300px; top: 12px; width: 82px; height: 82px; border-radius: 50%;
    background: radial-gradient(circle at 40% 35%, #f6e08a, #c9992b 70%, #9c7419); }
  .award-cover { top: 16px; width: 44px; height: 79px; background: linear-gradient(#2b2b2b, #0c0c0c); border: 2px solid #e5e5e5; }

  .footer { position: absolute; left: 0; top: 945px; width: 867px; height: 209px; background: var(--footer-black); }
  .footer-note { position: absolute; left: 49px; top: 27px; width: 378px; color: var(--white); font-size: 12.6px; line-height: 19.5px; }
  .footer-contact { position: absolute; left: 500px; top: 13px; width: 360px; color: var(--footer-text); font-size: 12.4px; line-height: 18px; }
  .footer-contact h3 { color: var(--accent-blue); font-size: 12.6px; font-weight: 700; line-height: 18px; }
  .footer-contact .block { margin-bottom: 16px; }

  .site-bar { position: absolute; left: 0; top: 1154px; width: 867px; height: 46px; background: var(--base-gray);
    color: var(--ink); font-weight: 700; font-size: 12px; text-align: center; line-height: 46px; }
</style>
</head>
<body>
<div class="letter">

  <header class="brand">
    <span class="brand-square"></span>
    <span class="brand-name">Harbor Ridge<br>Management &amp; Research, Inc.</span>
  </header>

  <div class="issue-date"><b>january</b> 12</div>

  <svg class="hero" viewBox="0 135 867 282" width="867" height="282" aria-hidden="false">
    <defs>
      <linearGradient id="heroTone" x1="0" y1="0" x2="1" y2="1">
        <stop offset="0" stop-color="#c9dcea"/>
        <stop offset="0.45" stop-color="#8fb3cf"/>
        <stop offset="1" stop-color="#d9e8f2"/>
      </linearGradient>
    </defs>
    <polygon role="img" aria-label="Photo: business people in suits walking through a bright glass office corridor"
      points="336,135 867,135 867,416 449,416" fill="url(#heroTone)"/>
    <polygon points="0,182 325,182 444,404 0,404" fill="var(--band-black)"/>
  </svg>
  <h1 class="hero-title">Title<br>here</h1>

  <main class="letter-body">
    <p>"Lorem ipsum dolor sit amet, consectetur adipiscing elit, sed do eiusmod tempor incididunt ut labore et dolore magna aliqua. Ut enim ad minim veniam, quis nostrud exercitation ullamco laboris nisi ut aliquip ex ea commodo consequat. Duis aute irure dolor in reprehenderit in voluptate velit esse cillum dolore eu fugiat nulla pariatur. Excepteur sint occaecat cupidatat non proident, sunt in culpa qui officia deserunt mollit anim id est laborum."</p>
    <p>"Lorem ipsum dolor sit amet, consectetur adipiscing elit, sed do eiusmod tempor incididunt ut labore et dolore magna aliqua. Ut enim ad minim veniam, quis nostrud exercitation ullamco laboris nisi ut aliquip ex ea commodo consequat. Duis aute irure dolor in reprehenderit in voluptate velit esse cillum dolore eu fugiat nulla pariatur. Excepteur sint occaecat cupidatat non proident, sunt in culpa qui officia deserunt mollit anim id est laborum."</p>
    <p>"Lorem ipsum dolor sit amet, consectetur adipiscing elit, sed do eiusmod tempor incididunt ut labore et dolore magna aliqua. Ut enim ad minim veniam, quis nostrud exercitation ullamco laboris nisi ut aliquip ex ea commodo consequat. Duis aute irure dolor in reprehenderit in voluptate velit esse cillum dolore eu fugiat nulla pariatur. Excepteur sint occaecat cupidatat non proident, sunt in culpa qui officia deserunt mollit anim id est laborum."</p>
  </main>

  <section class="awards" aria-label="Awards">
    <div class="award award-plaque" role="img" aria-label="Award badge"></div>
    <span class="awards-divider" style="left:238px"></span>
    <div class="award award-seal" role="img" aria-label="Award seal"></div>
    <span class="awards-divider" style="left:446px"></span>
    <div class="award award-cover" style="left:525px" role="img" aria-label="Award listing cover"></div>
    <span class="awards-divider" style="left:657px"></span>
    <div class="award award-cover" style="left:733px" role="img" aria-label="Award listing cover"></div>
  </section>

  <footer class="footer">
    <p class="footer-note">"Lorem ipsum dolor sit amet, consectetur adipiscing elit, sed do eiusmod tempor incididunt ut labore et dolore magna aliqua. Ut enim ad minim veniam, quis nostrud exercitation ullamco laboris nisi ut aliquip ex ea commodo consequat. Duis aute irure dolor in reprehenderit in voluptate velit esse cillum dolore eu fugiat nulla pariatur. Excepteur sint occaecat cupidatat non proident, sunt in culpa qui officia deserunt mollit anim id est laborum."</p>
    <div class="footer-contact">
      <div class="block">
        <h3>Harbor Ridge Management and Research Office Location</h3>
        2290 Linden Park STE 310<br>Brookfield, TX 77410
      </div>
      <div class="block">
        <h3>Mailing Address</h3>
        880 North Alder STE 204 #118<br>Brookfield, TX 77412
      </div>
      <div class="block">
        P: 555-214-7700<br>F: 888-555-0192<br>E: info@harborridgemr.com
      </div>
    </div>
  </footer>

  <div class="site-bar">www.harborridgemr.com</div>
</div>
</body>
</html>
```